Quick Start Orvane App Design Required!

We're designing an app to revolutionize data collection for outdoor works and road repairs. The app is currently being developed on Orvane and is due for launch later this year. We've created some functional wireframes that show how the app is to behave. We need you to make them look amazing!

Our intended audience is non-technical, and we'll need the app to be easy to navigate. We need a clean interface that is consistent with the Orvane interface. We expect you to use common Orvane design components and we're open to using the new Orvane Plinth design language.

We've included a set of wireframes that should show you what we're thinking, there are 12 screens that we need designed. We need your input on colors, fonts, layouts, and borders. If you use images, we'd prefer to see them only on the landing page.

To make things even easier, we have included designs for our website to show you what kind of design we like. Obviously we'd like to keep a consistent theme between the app and the website. We've included a copy of the logo for you to use where necessary too. Take note that we retain copyright to all materials included with this request.
Updates

Project Deadline Extended
Reason: We have decided to extend the deadline. There has been some late interest shown in the project and we'd like to give these designers the opportunity to refine their submissions.

Target Market(s)

Outdoor workers.

Industry/Entity Type

Orvane

Font styles to use
Serif
Sans Serif

Colors
3176b5

Requirements
Must have
• See the brief, all pages, designed as per brief.
Nice to have
• N/A
Should not have
• Too many images, please keep the design clean and simple.

```html
<!DOCTYPE html>
<html lang="en">
<head>
<meta charset="utf-8">
<title>Account Setup</title>
<link rel="stylesheet" href="https://fonts.googleapis.com/css2?family=Titillium+Web:wght@300;400&display=swap">
<style>
  :root {
    --page-bg: #e8ecf2;
    --progress-1: #9fd0f2;
    --progress-2: #27a2e0;
    --progress-3: #3176b5;
    --status-bar: #2a3139;
    --header-bg: #36444f;
    --body-bg: #252f3a;
    --field-bg: #ffffff;
    --placeholder: #b9ddf3;
    --text-light: #e4e8ec;
    --box-off: #526471;
    --box-on: #3176b5;
  }
  * { box-sizing: border-box; margin: 0; padding: 0; }
  html, body { width: 900px; height: 1200px; overflow: hidden; }
  body {
    background: var(--page-bg);
    font-family: "Titillium Web", sans-serif;
    font-weight: 300;
    position: relative;
  }
  .screen {
    position: absolute;
    left: 221px;
    top: 160px;
    width: 450px;
    height: 801px;
    background: var(--body-bg);
    overflow: hidden;
  }
  .progress { display: flex; height: 8px; }
  .progress span { flex: 1; }
  .progress .step-1 { background: var(--progress-1); }
  .progress .step-2 { background: var(--progress-2); }
  .progress .step-3 { background: var(--progress-3); }
  .status-bar { height: 7px; background: var(--status-bar); }
  .app-header {
    height: 86px;
    background: var(--header-bg);
    display: flex;
    align-items: center;
    justify-content: center;
    position: relative;
  }
  .back-button { position: absolute; left: 24px; top: 29px; width: 16px; height: 28px; }
  .app-title {
    color: var(--text-light);
    font-size: 25px;
    font-weight: 300;
    letter-spacing: 0.2px;
  }
  .setup-form { padding: 34px 29px 0 29px; }
  .field {
    display: block;
    height: 59px;
    background: var(--field-bg);
    color: var(--placeholder);
    font-size: 20px;
    line-height: 59px;
    padding-left: 21px;
    margin-bottom: 9px;
  }
  .section-label {
    color: var(--text-light);
    font-size: 20px;
    margin-top: 22px;
    margin-bottom: 8px;
  }
  .option-list { list-style: none; }
  .option {
    display: flex;
    align-items: center;
    height: 46px;
    color: var(--text-light);
    font-size: 20px;
  }
  .checkbox {
    width: 29px;
    height: 29px;
    background: var(--box-off);
    margin-right: 31px;
    display: flex;
    align-items: center;
    justify-content: center;
  }
  .option.is-checked .checkbox { background: var(--box-on); }
</style>
</head>
<body>
  <main class="screen">
    <div class="progress"><span class="step-1"></span><span class="step-2"></span><span class="step-3"></span></div>
    <div class="status-bar"></div>
    <header class="app-header">
      <svg class="back-button" viewBox="0 0 16 28" aria-label="Back">
        <polyline points="13,3 3,14 13,25" fill="none" stroke="#e4e8ec" stroke-width="2.4"/>
      </svg>
      <h1 class="app-title">ACCOUNT SETUP</h1>
    </header>
    <form class="setup-form">
      <span class="field">Name</span>
      <span class="field">Organisation</span>
      <span class="field">Team</span>
      <span class="field">Office Email</span>
      <p class="section-label">Enable Selection</p>
      <ul class="option-list">
        <li class="option"><span class="checkbox"></span>Roads</li>
        <li class="option is-checked"><span class="checkbox"><svg width="16" height="12" viewBox="0 0 16 12"><polyline points="2,6 6,10 14,2" fill="none" stroke="#fff" stroke-width="2.6"/></svg></span>Parks &amp; Garden</li>
        <li class="option"><span class="checkbox"></span>Electrical</li>
        <li class="option"><span class="checkbox"></span>Structures</li>
        <li class="option is-checked"><span class="checkbox"><svg width="16" height="12" viewBox="0 0 16 12"><polyline points="2,6 6,10 14,2" fill="none" stroke="#fff" stroke-width="2.6"/></svg></span>Tunnels</li>
        <li class="option"><span class="checkbox"></span>Depot</li>
        <li class="option is-checked"><span class="checkbox"><svg width="16" height="12" viewBox="0 0 16 12"><polyline points="2,6 6,10 14,2" fill="none" stroke="#fff" stroke-width="2.6"/></svg></span>Linemarking</li>
      </ul>
    </form>
  </main>
</body>
</html>
```